"Retire With The Harrowgate Fund" Book Cover Design

This book is 5.5 x. 8.5 in size. Not enough room for any writing on the spine either. About 100 pages, and 18,000 words max.
The Harrowgate Fund goes back to 1930. In this book, I run scenario after scenario seeing what the best strategy was for someone to Retire With The Harrowgate Fund and never run out of money. And how they MIGHT be able to use this info to build a solid retirement plan using the Harrowgate Fund for themselves.
Target Market(s)
Soon-to-be and recent middle-class, married retirees.
Industry/Entity Type
Investment Advisory
Requirements
Must have
- MUST BE EYE CATCHING!
Should not have
- No Piggy Banks or old people sitting on a beach or any yachts.

```html
<!DOCTYPE html>
<html lang="en">
<head>
<meta charset="utf-8">
<title>Retire With The Harrowgate Fund – Book Cover</title>
<link href="https://fonts.googleapis.com/css2?family=Ultra&display=swap" rel="stylesheet">
<style>
  :root {
    --page-bg: #e4e3e3;
    --green-deep: #00903e;
    --green-bright: #24a038;
    --title-white: #f5f5f5;
    --title-gold: #f2c200;
  }
  * { margin: 0; padding: 0; box-sizing: border-box; }
  html, body {
    width: 1035px;
    height: 1200px;
    overflow: hidden;
    background: var(--page-bg);
  }
  .stage {
    width: 1035px;
    height: 1200px;
    display: flex;
    justify-content: center;
    align-items: center;
  }
  .book-cover {
    width: 776px;
    height: 1200px;
    display: block;
  }
  .cover-title {
    font-family: "Ultra", Georgia, serif;
    fill: var(--title-white);
  }
  .cover-title .title-name { fill: var(--title-gold); }
  .band-deep { fill: var(--green-deep); }
  .band-bright { fill: var(--green-bright); }
  .rising-arrow { fill: var(--title-white); }
</style>
</head>
<body>
  <main class="stage">
    <svg class="book-cover" viewBox="0 0 776 1200" role="img" aria-label="Book cover: Retire With The Harrowgate Fund">
      <rect class="band-deep" x="0" y="0" width="776" height="1200"/>
      <polygon class="band-bright" points="0,698 387,556 776,698 776,1200 0,1200"/>

      <text class="cover-title">
        <tspan x="83" y="204" font-size="133" textLength="609" lengthAdjust="spacingAndGlyphs">RETIRE</tspan>
        <tspan x="212" y="266" font-size="55" textLength="348" lengthAdjust="spacingAndGlyphs">WITH THE</tspan>
        <tspan class="title-name" x="85" y="338" font-size="74" textLength="606" lengthAdjust="spacingAndGlyphs">HARROWGATE</tspan>
        <tspan x="84" y="488" font-size="178" textLength="608" lengthAdjust="spacingAndGlyphs">FUND</tspan>
      </text>

      <polygon class="rising-arrow" points="387,594 549,829 387,795 226,829"/>
    </svg>
  </main>
</body>
</html>
```